Our Kitchen Pantry is an online food market place that connects foodies who make or grow great food with

We would like a 1/2 A4 page size flyer in landscape to promote our new business. We would like to encourage new home foodies to sign up for a membership on our website www.ourkitchenpantrynz.co.nz and we would like customers who are looking for great food in their local community to search our website for their closest home foodie and support a neighbour who is growing or producing creative food locally

Target Market(s)

Creative food lovers

Industry/Entity Type

Landscape

Colors
acd037
f78f20
33b8a4

Requirements
Must have
• Food images and look groovy
• Must be easy to read and stand out on a notice board
• Website address www.ourkitchenpantrynz.co.nz
Nice to have
• We wish to use this flyer in multiple locations and wish to put in different contact details prior to printing

```html
<!DOCTYPE html>
<html lang="en">
<head>
<meta charset="utf-8">
<title>Our Kitchen Pantry – Flyer</title>
<link rel="stylesheet" href="https://fonts.googleapis.com/css2?family=Fira+Sans+Condensed:wght@500;700&family=PT+Sans:wght@400&display=swap">
<style>
  :root {
    --backdrop: #a3a3a3;
    --paper: #ffffff;
    --leaf-green: #80b940;
    --cocoa: #523220;
    --ink: #1e1e1e;
    --photo-light: #efe6dc;
    --photo-mid: #d4c2b0;
    --photo-salad: #8dbb5a;
  }
  * { box-sizing: border-box; margin: 0; padding: 0; }
  html, body {
    width: 1200px; height: 911px; overflow: hidden;
    background: var(--backdrop);
  }
  .flyer {
    position: absolute; left: 116px; top: 117px;
    width: 968px; height: 678px;
    background: var(--paper);
    overflow: hidden;
  }
  .flyer-shapes { position: absolute; inset: 0; width: 968px; height: 678px; }
  .brand {
    position: absolute; left: 150px; top: 50px; width: 240px;
    display: flex; align-items: center; gap: 14px;
  }
  .brand-dot {
    flex: none; width: 30px; height: 30px; border-radius: 50%;
    background: var(--leaf-green);
  }
  .brand-name {
    font-family: "Fira Sans Condensed", "Arial Narrow", sans-serif;
    font-weight: 700; font-size: 44px; line-height: 0.98;
    color: var(--cocoa); text-transform: uppercase;
  }
  .headline {
    position: absolute; left: 20px; top: 265px; width: 500px;
    text-align: center; color: var(--paper);
    font-family: "Fira Sans Condensed", "Arial Narrow", sans-serif;
    font-weight: 500; font-size: 30px; line-height: 40px;
  }
  .benefits {
    position: absolute; left: 20px; top: 425px; width: 500px;
    text-align: center; color: var(--ink);
    font-family: "PT Sans", Arial, sans-serif;
    font-size: 15.5px; line-height: 20px;
  }
  .benefits p + p { margin-top: 14px; }
  .contact {
    position: absolute; left: 20px; top: 584px; width: 510px;
    text-align: center; color: var(--paper);
    font-family: "PT Sans", Arial, sans-serif;
  }
  .contact-lead { font-size: 19px; line-height: 22px; }
  .contact-url {
    font-family: "Fira Sans Condensed", "Arial Narrow", sans-serif;
    font-weight: 700; font-size: 32px; line-height: 40px;
  }
</style>
</head>
<body>
  <main class="flyer">
    <svg class="flyer-shapes" viewBox="0 0 968 678" aria-hidden="false">
      <defs>
        <linearGradient id="kitchen-tones" x1="0" y1="0" x2="0" y2="1">
          <stop offset="0" stop-color="var(--photo-light)"/>
          <stop offset="0.6" stop-color="var(--photo-mid)"/>
          <stop offset="1" stop-color="var(--photo-salad)"/>
        </linearGradient>
      </defs>
      <path class="headline-band" fill="var(--leaf-green)"
        d="M0 243 H500 Q520 258 508 275 Q498 295 514 312 Q526 330 508 350 Q496 370 512 388 Q520 402 505 409 H0 Z"/>
      <rect class="footer-band" x="0" y="556" width="968" height="122" fill="var(--cocoa)"/>
      <path class="kitchen-photo" role="img" aria-label="Photo: smiling cook in a striped apron tossing a fresh salad in a glass bowl in a bright kitchen"
        fill="url(#kitchen-tones)" stroke="var(--paper)" stroke-width="4"
        d="M600 40 Q640 0 680 20 Q720 5 760 15 Q800 0 840 20 Q880 35 920 30 L968 40 V640
           Q940 672 900 660 Q860 680 820 655 Q780 672 740 645 Q700 652 675 620 Q640 600 612 570
           Q590 532 585 500 Q520 470 515 430 Q505 390 515 350 Q505 310 525 270 Q518 230 545 195
           Q530 150 560 110 Q560 70 600 40 Z"/>
    </svg>

    <div class="brand">
      <span class="brand-dot"></span>
      <span class="brand-name">Our Kitchen<br>Pantry</span>
    </div>

    <h1 class="headline">Be part of our exciting new<br>online food marketplace connecting<br>foodies in your local community</h1>

    <div class="benefits">
      <p># As a foodie you can sell your beautiful home produced<br>or home grown produce on our marketplace website</p>
      <p># As a food lover you can purchase lovingly grown or<br>prepared food and support your local foodie community<br>while keeping your food miles low</p>
    </div>

    <div class="contact">
      <p class="contact-lead">For more information go to:</p>
      <p class="contact-url">www.ourkitchenpantrynz.co.nz</p>
    </div>
  </main>
</body>
</html>
```